Design WORDPRESS Website for E Commerce Business

We are needing a WORDPRESS website for an E Commerce Business that is supplying quailty kids / baby products.

Target Market(s)

Female / Working Mums / New Mums

Industry/Entity Type

Business

Number of Pages Required

1 page

Font styles to use
Sans Serif

Colors
33b8a4
f8fcfd
d3a5cc
f7f1f7
cbcbcb
9d9d9d

```html
<!DOCTYPE html>
<html lang="en">
<head>
<meta charset="utf-8">
<title>Nest &amp; Nook — Kids Collections</title>
<link rel="stylesheet" href="https://fonts.googleapis.com/css2?family=Lora:wght@400;700&family=Open+Sans:wght@400;600;700&display=swap">
<style>
:root{
  --teal:#33b8a4;
  --teal-dark:#2aa08e;
  --lilac:#d3a5cc;
  --lilac-band:#c79bc0;
  --lilac-soft:#f7f1f7;
  --ice:#f8fcfd;
  --line:#cbcbcb;
  --muted:#9d9d9d;
  --ink:#333333;
  --ink-soft:#555555;
  --white:#ffffff;
  --gold:#a79a2a;
}
*{box-sizing:border-box;margin:0;padding:0}
html,body{width:1200px;height:2936px;overflow:hidden}
body{position:relative;background:var(--white);font-family:"Open Sans",Arial,sans-serif;color:var(--ink)}
.abs{position:absolute}
a{color:inherit;text-decoration:none}

/* header */
.brand{left:106px;top:16px;display:flex;align-items:center;gap:12px}
.brand-dot{width:56px;height:56px;border-radius:50%;background:var(--muted)}
.brand-name{font-family:"Lora",Georgia,serif;font-weight:700;font-size:34px;line-height:1;color:var(--teal);width:110px}
.topbar{top:14px;left:590px;display:flex;align-items:center;gap:26px;font-family:"Lora",Georgia,serif;font-size:14px;font-weight:700}
.topbar .tool{display:flex;align-items:center;gap:8px}
.topbar svg{width:13px;height:13px;fill:var(--teal)}
.search{width:196px;height:34px;border:1px solid var(--line);border-radius:17px;display:flex;align-items:center;justify-content:space-between;padding:0 14px;font-size:13px;font-weight:400;color:var(--muted);font-family:"Open Sans",Arial,sans-serif}
.search svg{fill:var(--ink)}
.cart-btn{background:var(--teal);color:var(--white);height:36px;padding:0 18px;border-radius:18px;display:flex;align-items:center;gap:8px}
.cart-btn svg{fill:var(--white)}
.nav{top:70px;right:98px;display:flex;gap:34px;font-family:"Lora",Georgia,serif;font-weight:700;font-size:14px;color:var(--ink)}
.nav .active{color:var(--teal);border-bottom:2px solid var(--teal);padding-bottom:4px}

/* hero */
.hero{left:0;top:104px;width:1200px;height:477px;background:linear-gradient(90deg,#f08a1c 0%,#f39a2a 45%,#ee8618 100%)}
.hero-photo{position:absolute;left:160px;top:0;width:640px;height:477px;background:linear-gradient(180deg,#7fa6cc 0%,#9fbcd9 60%,#c8d6e4 100%);opacity:.55}
.hero-title{position:absolute;left:0;right:0;top:278px;line-height:56px;text-align:center;font-family:"Lora",Georgia,serif;font-size:44px;letter-spacing:16px;color:var(--white);font-weight:400}
.btn-shop{position:absolute;left:532px;top:372px;width:134px;height:40px;border-radius:20px;background:var(--teal);color:var(--white);font-family:"Lora",Georgia,serif;font-weight:700;font-size:14px;display:flex;align-items:center;justify-content:center}

/* category tiles */
.tile{top:589px;height:209px}
.tile-frame{position:absolute;inset:8px;border:2px solid rgba(255,255,255,.9);display:flex;font-family:"Lora",Georgia,serif;font-weight:700;font-size:19px;color:var(--white);text-shadow:0 1px 3px rgba(0,0,0,.35)}
.tile-a{left:0;width:395px;background:linear-gradient(135deg,#c9c6c4,#e5e2df)}
.tile-a .tile-frame{align-items:flex-end;padding:0 0 20px 82px}
.tile-b{left:405px;width:393px;background:linear-gradient(135deg,#a9c3d8,#d7e4ee 55%,#e9d46a 85%)}
.tile-b .tile-frame{align-items:flex-start;justify-content:center;padding-top:58px}
.tile-c{left:808px;width:392px;background:linear-gradient(135deg,#7d7264,#c9b7a3 50%,#2a4f9a)}
.tile-c .tile-frame{align-items:flex-end;justify-content:flex-end;padding:0 22px 26px 0}

/* tabs */
.tabs-rule{left:100px;top:863px;width:1000px;height:1px;background:var(--line)}
.tabs{left:100px;top:865px;display:flex;gap:3px;font-family:"Lora",Georgia,serif;font-size:13px;color:var(--white)}
.tab{height:41px;display:flex;align-items:center;justify-content:center;background:var(--lilac)}
.tab.active{background:var(--teal)}

/* product cards */
.grid{left:100px;display:flex;gap:10px}
.card{width:243px;height:385px;border:1px solid #e3e3e3;background:var(--white);position:relative}
.card-img{position:absolute;left:30px;top:22px;width:183px;height:230px;border-radius:6px}
.stars{position:absolute;right:12px;top:280px;font-size:12px;letter-spacing:1px;color:var(--gold)}
.stars .off{color:var(--line)}
.card-title{position:absolute;left:0;right:0;top:310px;text-align:center;font-size:13px;color:var(--ink-soft)}
.price{position:absolute;left:14px;top:346px;width:66px;height:26px;border-radius:13px;background:var(--teal);color:var(--white);font-size:12px;font-weight:600;display:flex;align-items:center;justify-content:center}
.actions{position:absolute;right:14px;top:344px;display:flex;gap:7px}
.act{width:28px;height:28px;border-radius:50%;background:var(--lilac);display:flex;align-items:center;justify-content:center}
.act svg{width:14px;height:14px;fill:var(--white)}

/* offers */
.offer-band{left:0;top:1390px;width:1200px;height:199px;background:var(--ice)}
.offer{top:1405px;width:495px;height:170px}
.offer-frame{position:absolute;inset:8px;border:1.5px solid rgba(255,255,255,.85);display:flex;align-items:center;justify-content:center;font-family:"Lora",Georgia,serif;font-weight:700;font-size:28px;color:var(--white);letter-spacing:1px}
.offer-a{left:100px;background:linear-gradient(120deg,#1e160f,#3d2c1d 50%,#241a12)}
.offer-b{left:605px;background:linear-gradient(120deg,#5e5e5a,#8b8579 50%,#4a4a48)}

/* featured */
.featured-bar{left:100px;top:1648px;width:1000px;height:64px;background:var(--teal);color:var(--white);font-family:"Lora",Georgia,serif;font-weight:700;font-size:26px;letter-spacing:1px;display:flex;align-items:center;padding-left:28px}
.pager{top:2158px;left:1034px;display:flex;gap:12px}
.pager span{width:26px;height:26px;border-radius:50%;background:#2e2e2e;display:flex;align-items:center;justify-content:center}
.pager svg{width:10px;height:10px;fill:var(--white)}

/* service band */
.service-band{left:0;top:2235px;width:1200px;height:157px;background:var(--lilac-band)}
.service{top:2260px;height:106px;background:var(--white);display:flex;align-items:center;gap:14px;padding-left:14px}
.service-icon{width:54px;height:54px;border-radius:50%;background:var(--teal);display:flex;align-items:center;justify-content:center;flex:none}
.service-icon svg{width:26px;height:26px;fill:var(--white)}
.service h3{font-family:"Lora",Georgia,serif;font-weight:700;font-size:16px;color:var(--ink);letter-spacing:.5px}
.service p{font-size:12px;color:var(--ink-soft);margin-top:4px}

/* footer */
.rule{left:100px;width:1000px;height:1px;background:#e0e0e0}
.foot-links{top:2536px;right:346px;display:flex;gap:26px;font-family:"Lora",Georgia,serif;font-size:13px;color:var(--ink);white-space:nowrap}
.socials{top:2526px;left:898px;display:flex;gap:14px}
.socials span{width:40px;height:40px;border-radius:50%}
.col{top:2643px;font-family:"Lora",Georgia,serif;font-size:12.5px;line-height:24px;color:var(--ink-soft)}
.contact{top:2643px;left:420px;width:330px;text-align:center;font-family:"Lora",Georgia,serif;font-size:12px;line-height:24px;color:var(--ink-soft)}
.cards{top:2720px;left:456px;display:flex;gap:10px}
.cards span{width:40px;height:28px;border-radius:4px}
.newsletter{left:810px;top:2640px;width:290px}
.newsletter h4{font-family:"Lora",Georgia,serif;font-weight:700;font-size:19px;color:var(--ink)}
.newsletter p{font-family:"Lora",Georgia,serif;font-size:12.5px;line-height:23px;color:var(--ink-soft);margin-top:10px}
.field{margin-top:16px;height:36px;border:1px solid #e0e0e0;font-size:12px;color:var(--muted);display:flex;align-items:center;padding-left:12px}
.subscribe{margin-top:12px;height:32px;background:var(--lilac);color:var(--white);font-family:"Lora",Georgia,serif;font-size:13px;letter-spacing:1px;display:flex;align-items:center;justify-content:center}
.copyright{top:2890px;left:0;width:1200px;text-align:center;font-family:"Lora",Georgia,serif;font-size:12px;color:var(--ink-soft)}
</style>
</head>
<body>

<svg width="0" height="0" style="position:absolute" aria-hidden="true">
  <defs>
    <symbol id="i-heart" viewBox="0 0 24 24"><path d="M12 21l-1.5-1.3C5 15 2 12.2 2 8.5 2 5.5 4.4 3 7.4 3c1.7 0 3.4.8 4.6 2.1C13.2 3.8 14.9 3 16.6 3 19.6 3 22 5.5 22 8.5c0 3.7-3 6.5-8.5 11.2z"/></symbol>
    <symbol id="i-eye" viewBox="0 0 24 24"><path d="M12 5C6 5 2 12 2 12s4 7 10 7 10-7 10-7-4-7-10-7zm0 11a4 4 0 110-8 4 4 0 010 8zm0-6a2 2 0 100 4 2 2 0 000-4z"/></symbol>
    <symbol id="i-cart" viewBox="0 0 24 24"><path d="M3 3h3l2.5 11h10l2.5-8H8M9 19a2 2 0 104 0 2 2 0 00-4 0zm7 0a2 2 0 104 0 2 2 0 00-4 0z"/></symbol>
    <symbol id="i-lock" viewBox="0 0 24 24"><path d="M6 10V7a6 6 0 0112 0v3h1v12H5V10zm3 0h6V7a3 3 0 00-6 0z"/></symbol>
    <symbol id="i-pen" viewBox="0 0 24 24"><path d="M3 17.3V21h3.7L18 9.7 14.3 6zM20.7 7a1 1 0 000-1.4l-2.3-2.3a1 1 0 00-1.4 0l-1.8 1.8L19 8.8z"/></symbol>
    <symbol id="i-search" viewBox="0 0 24 24"><path d="M10 2a8 8 0 016.3 12.9l5.4 5.4-1.4 1.4-5.4-5.4A8 8 0 1110 2zm0 3a5 5 0 100 10 5 5 0 000-10z"/></symbol>
    <symbol id="i-plane" viewBox="0 0 24 24"><path d="M21 16v-2l-8-5V3.5a1.5 1.5 0 00-3 0V9l-8 5v2l8-2.5V19l-2 1.5V22l3.5-1 3.5 1v-1.5L13 19v-5.5z"/></symbol>
    <symbol id="i-sync" viewBox="0 0 24 24"><path d="M12 4V1L8 5l4 4V6a6 6 0 016 6 6 6 0 01-.7 2.8l1.5 1.5A8 8 0 0012 4zm0 14a6 6 0 01-6-6 6 6 0 01.7-2.8L5.2 7.7A8 8 0 0012 20v3l4-4-4-4z"/></symbol>
    <symbol id="i-chat" viewBox="0 0 24 24"><path d="M12 3C6.5 3 2 6.6 2 11c0 2.3 1.2 4.3 3.1 5.8L4 21l4.5-2.4c1.1.3 2.3.4 3.5.4 5.5 0 10-3.6 10-8s-4.5-8-10-8z"/></symbol>
    <symbol id="i-thumb" viewBox="0 0 24 24"><path d="M2 21h4V9H2zm20-11a2 2 0 00-2-2h-6.3l1-4.6v-.3a1.5 1.5 0 00-.4-1L13.2 1 7.6 6.6A2 2 0 007 8v11a2 2 0 002 2h9a2 2 0 001.8-1.2l3-7.1c.1-.2.2-.5.2-.7z"/></symbol>
    <symbol id="i-left" viewBox="0 0 24 24"><path d="M16 3L7 12l9 9 2-2-7-7 7-7z"/></symbol>
    <symbol id="i-right" viewBox="0 0 24 24"><path d="M8 3l9 9-9 9-2-2 7-7-7-7z"/></symbol>
  </defs>
</svg>

<header>
  <div class="brand abs">
    <span class="brand-dot"></span>
    <span class="brand-name">Nest &amp; Nook</span>
  </div>
  <div class="topbar abs">
    <a class="tool" href="#"><svg><use href="#i-lock"/></svg>Login</a>
    <a class="tool" href="#"><svg><use href="#i-pen"/></svg>Sign Up</a>
    <div class="search">Search<svg width="13" height="13"><use href="#i-search"/></svg></div>
    <a class="cart-btn" href="#"><svg><use href="#i-cart"/></svg>My Cart (0)</a>
  </div>
  <nav class="nav abs">
    <a class="active" href="#">Home</a><a href="#">About Us</a><a href="#">Services</a><a href="#">Products</a><a href="#">Accessories</a><a href="#">Blog</a><a href="#">Contact Us</a>
  </nav>
</header>

<section class="hero abs">
  <div class="hero-photo" role="img" aria-label="Photo of a mother and young daughter in denim jackets and sunglasses against an orange wall"></div>
  <h1 class="hero-title">KIDS COLLECTIONS</h1>
  <a class="btn-shop" href="#">SHOP NOW</a>
</section>

<section>
  <div class="tile tile-a abs" role="img" aria-label="Photo of a newborn baby sleeping on a dotted blanket"><div class="tile-frame">Born Babies Collections</div></div>
  <div class="tile tile-b abs" role="img" aria-label="Photo of a baby wrapped in a yellow hooded towel"><div class="tile-frame">New Collections</div></div>
  <div class="tile tile-c abs" role="img" aria-label="Photo of folded kids clothes and a toy truck"><div class="tile-frame">Toys Games</div></div>
</section>

<div class="tabs-rule abs"></div>
<div class="tabs abs">
  <span class="tab active" style="width:129px">Most popular</span>
  <span class="tab" style="width:125px">Top Rated</span>
  <span class="tab" style="width:131px">Latest Arrivals</span>
</div>

<section class="grid abs" style="top:961px">
  <article class="card"><div class="card-img" role="img" aria-label="Navy and white striped kids sweater" style="background:linear-gradient(180deg,#2b2f6e,#dfe0ea)"></div><div class="stars">★★★★<span class="off">★</span></div><p class="card-title">Combined with a handful of model</p><span class="price">$98.00</span><div class="actions"><span class="act"><svg><use href="#i-heart"/></svg></span><span class="act"><svg><use href="#i-eye"/></svg></span><span class="act"><svg><use href="#i-cart"/></svg></span></div></article>
  <article class="card"><div class="card-img" role="img" aria-label="Pink sleeveless girls dress" style="background:linear-gradient(180deg,#e8b3b0,#f3d1cd)"></div><div class="stars">★★★★<span class="off">★</span></div><p class="card-title">Combined with a handful of model</p><span class="price">$98.00</span><div class="actions"><span class="act"><svg><use href="#i-heart"/></svg></span><span class="act"><svg><use href="#i-eye"/></svg></span><span class="act"><svg><use href="#i-cart"/></svg></span></div></article>
  <article class="card"><div class="card-img" role="img" aria-label="Dark grey kids winter parka with fur hood" style="background:linear-gradient(180deg,#6b5a44,#3d4250)"></div><div class="stars">★★★★<span class="off">★</span></div><p class="card-title">Combined with a handful of model</p><span class="price">$98.00</span><div class="actions"><span class="act"><svg><use href="#i-heart"/></svg></span><span class="act"><svg><use href="#i-eye"/></svg></span><span class="act"><svg><use href="#i-cart"/></svg></span></div></article>
  <article class="card"><div class="card-img" role="img" aria-label="Light pink dotted kids sweatshirt" style="background:linear-gradient(180deg,#f0aec0,#f6cfd9)"></div><div class="stars">★★★★<span class="off">★</span></div><p class="card-title">Combined with a handful of model</p><span class="price">$98.00</span><div class="actions"><span class="act"><svg><use href="#i-heart"/></svg></span><span class="act"><svg><use href="#i-eye"/></svg></span><span class="act"><svg><use href="#i-cart"/></svg></span></div></article>
</section>

<section>
  <div class="offer-band abs"></div>
  <div class="offer offer-a abs" role="img" aria-label="Dark photo with warm bokeh lights and a gold star"><div class="offer-frame">GET&nbsp; SUMMER OFFERS</div></div>
  <div class="offer offer-b abs" role="img" aria-label="Photo of a kids clothing shop interior"><div class="offer-frame">LATEST COLLETIONS</div></div>
</section>

<h2 class="featured-bar abs">FEATURED</h2>

<section class="grid abs" style="top:1771px">
  <article class="card"><div class="card-img" role="img" aria-label="Photo of a baby girl in a red dress" style="background:linear-gradient(180deg,#f4f1ef,#d8455a 70%,#f4f1ef)"></div><div class="stars">★★★★<span class="off">★</span></div><p class="card-title">Combined with a handful of model</p><span class="price">$98.00</span><div class="actions"><span class="act"><svg><use href="#i-heart"/></svg></span><span class="act"><svg><use href="#i-eye"/></svg></span><span class="act"><svg><use href="#i-cart"/></svg></span></div></article>
  <article class="card"><div class="card-img" role="img" aria-label="Photo of a baby in a knitted hat and white bodysuit" style="background:linear-gradient(180deg,#f4f1ef,#cfc9c2 60%,#f4f1ef)"></div><div class="stars">★★★★<span class="off">★</span></div><p class="card-title">Combined with a handful of model</p><span class="price">$98.00</span><div class="actions"><span class="act"><svg><use href="#i-heart"/></svg></span><span class="act"><svg><use href="#i-eye"/></svg></span><span class="act"><svg><use href="#i-cart"/></svg></span></div></article>
  <article class="card"><div class="card-img" role="img" aria-label="Photo of a toddler in striped green and blue pyjamas" style="background:linear-gradient(180deg,#f4f1ef,#4b8fa8 55%,#f4f1ef)"></div><div class="stars">★★★★<span class="off">★</span></div><p class="card-title">Combined with a handful of model</p><span class="price">$98.00</span><div class="actions"><span class="act"><svg><use href="#i-heart"/></svg></span><span class="act"><svg><use href="#i-eye"/></svg></span><span class="act"><svg><use href="#i-cart"/></svg></span></div></article>
  <article class="card"><div class="card-img" role="img" aria-label="Photo of a toddler in a yellow t-shirt" style="background:linear-gradient(180deg,#f4f1ef,#e8d23a 55%,#f4f1ef)"></div><div class="stars">★★★★<span class="off">★</span></div><p class="card-title">Combined with a handful of model</p><span class="price">$98.00</span><div class="actions"><span class="act"><svg><use href="#i-heart"/></svg></span><span class="act"><svg><use href="#i-eye"/></svg></span><span class="act"><svg><use href="#i-cart"/></svg></span></div></article>
</section>
<div class="pager abs"><span><svg><use href="#i-left"/></svg></span><span><svg><use href="#i-right"/></svg></span></div>

<section>
  <div class="service-band abs"></div>
  <div class="service abs" style="left:100px;width:238px"><span class="service-icon"><svg><use href="#i-plane"/></svg></span><div><h3>FAST DELIVERY</h3><p>On order over $199.00</p></div></div>
  <div class="service abs" style="left:352px;width:239px"><span class="service-icon"><svg><use href="#i-sync"/></svg></span><div><h3>EXCHANGE</h3><p>Money back in 30days</p></div></div>
  <div class="service abs" style="left:607px;width:238px"><span class="service-icon"><svg><use href="#i-chat"/></svg></span><div><h3>SUPPORT 247</h3><p>Alway online care customer</p></div></div>
  <div class="service abs" style="left:859px;width:239px"><span class="service-icon"><svg><use href="#i-thumb"/></svg></span><div><h3>NEW ARRIVAL</h3><p>Manufacturers Guarantee</p></div></div>
</section>

<footer>
  <div class="rule abs" style="top:2488px"></div>
  <nav class="foot-links abs"><a href="#">Company</a><a href="#">Affiliates</a><a href="#">Support</a><a href="#">Privacy</a><a href="#">Advance Search</a><a href="#">FAQ's</a></nav>
  <div class="socials abs"><span style="background:#3b6fc1"></span><span style="background:#2aa3e0"></span><span style="background:#d23a32"></span><span style="background:#d9822b"></span></div>
  <div class="rule abs" style="top:2609px"></div>

  <ul class="col abs" style="left:100px;list-style:none"><li>My Orders</li><li>My Personal Info</li><li>My Credit Slips</li><li>My Address</li><li>My History</li><li>Specials</li></ul>
  <ul class="col abs" style="left:268px;list-style:none"><li>Featured</li><li>New Arrivals</li><li>Careers</li><li>Search Terms</li><li>Orders &amp; Returns</li><li>Site Map</li></ul>

  <div class="contact abs">#12 Harbour Lane, North Wing, 2nd Floor, Australia .<br>Call us: 0400 123 456 / Email: hello@nestnook.example</div>
  <div class="cards abs"><span style="background:#2c72c6"></span><span style="background:#e38a2d"></span><span style="background:#1f3f8e"></span><span style="background:#35b3d0"></span><span style="background:#e0454d"></span></div>

  <div class="newsletter abs">
    <h4>Newsletter</h4>
    <p>Lorem ipsum dolor sit amet, consectetur adipiscing elit. Curabitur volutpat tincidunt facilisis.</p>
    <div class="field">Email Id...</div>
    <div class="subscribe">SUBSCRIBE</div>
  </div>

  <div class="rule abs" style="top:2861px"></div>
  <p class="copyright abs">Copyright © 2017 Brightfold. All rights reserved.</p>
</footer>

</body>
</html>
```